A4 Flyer

Bright Path Learning is starting a course in regional Victoria. We are currently advertising (See attached file A34984) in local papers but need to create a one page flyer to distribute to Aged Care facilities in the area. The A4 flyer will be inserted into a folder pack with more detailed information on Bright Path Learning. Important to use images and logoes attached

Target Market(s)

Flyer to be distributed to Aged Care facility staff and owners

Industry/Entity Type

Advertising

Font styles to use
Sans Serif

Colors
f37123
ec1f27

Requirements
Must have
• BPL Logo
Some image

```html
<!DOCTYPE html>
<html lang="en">
<head>
<meta charset="UTF-8">
<title>Bright Path Learning – Fast Track Course Flyer</title>
<link href="https://fonts.googleapis.com/css2?family=Open+Sans:wght@300;400;600;700&display=swap" rel="stylesheet">
<style>
  :root {
    --backdrop: #2f2f2f;
    --paper: #ffffff;
    --orange: #f37123;
    --orange-text: #e06a24;
    --red: #d8262e;
    --red-deep: #c91f27;
    --ink: #222222;
    --ink-soft: #333333;
    --grey: #555555;
    --ring: #9a9a9a;
  }
  * { box-sizing: border-box; margin: 0; padding: 0; }
  html, body {
    width: 1200px; height: 1000px; overflow: hidden;
    background: var(--backdrop);
    font-family: "Open Sans", Arial, sans-serif;
  }
  .flyer {
    position: absolute; left: 290px; top: 62px;
    width: 620px; height: 876px;
    background: var(--paper); overflow: hidden;
  }
  .bands { position: absolute; inset: 0; }
  .line { position: absolute; left: 0; width: 100%; text-align: center; white-space: nowrap; }
  .headline { top: 18px; font-size: 41px; font-weight: 300; letter-spacing: 6px; color: var(--ink-soft); }
  .course-start { top: 80px; font-size: 22px; color: var(--orange-text); }
  .qualification { top: 122px; font-size: 19px; font-weight: 700; line-height: 28px; color: var(--ink); letter-spacing: 0.5px; }
  .funding { top: 190px; font-size: 20px; letter-spacing: 1.5px; color: var(--ink); }
  .fees { top: 220px; font-size: 19px; letter-spacing: 1px; color: var(--ink); }
  .fees strong { color: var(--orange-text); font-weight: 700; }
  .delivery { top: 256px; font-size: 16px; line-height: 26px; color: var(--ink); }
  .venue { top: 312px; font-size: 24px; color: var(--orange-text); }
  .hours { top: 350px; font-size: 24px; color: var(--orange-text); }

  .brand {
    position: absolute; left: 322px; top: 398px;
    display: flex; align-items: center; gap: 12px;
  }
  .brand-dot { width: 56px; height: 56px; border-radius: 50%; background: var(--orange); }
  .brand-name { font-size: 30px; font-weight: 400; line-height: 32px; color: var(--grey); }

  .contact { position: absolute; right: 24px; text-align: right; white-space: nowrap; }
  .website { top: 493px; font-size: 16px; font-weight: 700; color: var(--orange-text); }
  .or-call { top: 537px; font-size: 23px; letter-spacing: 1.5px; color: var(--grey); }
  .phone { top: 586px; font-size: 23px; font-weight: 700; letter-spacing: 1px; color: var(--orange-text); }

  .photo {
    position: absolute; border-radius: 50%;
    border: 13px solid var(--ring);
  }
  .photo-tutor { left: 14px; top: 418px; width: 220px; height: 220px;
    background: linear-gradient(160deg, #eef0f2 0%, #d9dcdf 55%, #8a6a55 100%); }
  .photo-student { left: 236px; top: 548px; width: 170px; height: 170px;
    background: linear-gradient(160deg, #e9eaec 0%, #b9b4b2 50%, #2b2526 100%); }
  .photo-practical { left: 433px; top: 646px; width: 174px; height: 174px;
    background: linear-gradient(160deg, #f3efe9 0%, #d9c7b3 50%, #b0463c 100%); }

  .topics {
    position: absolute; left: 18px; top: 646px;
    list-style: none; color: #fff; font-size: 20px; line-height: 26px;
  }
  .topics li::before { content: "•"; }
</style>
</head>
<body>
  <main class="flyer">
    <svg class="bands" width="620" height="876" viewBox="0 0 620 876" aria-hidden="true">
      <defs>
        <linearGradient id="redBand" x1="0" y1="0" x2="0" y2="1">
          <stop offset="0" stop-color="#d9353b"/>
          <stop offset="1" stop-color="#c91f27"/>
        </linearGradient>
      </defs>
      <polygon points="0,423 620,768 620,876 0,876" fill="var(--orange)"/>
      <polygon points="0,446 620,800 620,876 0,876" fill="url(#redBand)"/>
    </svg>

    <h1 class="line headline">UNIQUE OPPORTUNITY</h1>
    <p class="line course-start">FAST TRACK COURSE - START JULY 2014</p>
    <p class="line qualification">Double Qualification - Cert III Aged Care With<br>Home and community care</p>
    <p class="line funding">GOVERNMENT FUNDING FOR ELIGIBLE STUDENTS!</p>
    <p class="line fees"><strong>FEES FROM $117</strong> TO ENROL VISIT</p>
    <p class="line delivery">THIS TRAINING IS DELIVERED WITH VIC<br>AND COMM GOVT FUNDING TO ELIGIBLE STUDENTS</p>
    <p class="line venue">GREENVALE NURSING Home - Stawell</p>
    <p class="line hours">9:00am - 3:00pm</p>

    <div class="brand">
      <span class="brand-dot"></span>
      <span class="brand-name">Bright Path<br>Learning</span>
    </div>

    <p class="contact website">www.brightpathlearning-com.au</p>
    <p class="contact or-call">OR CALL</p>
    <p class="contact phone">9123 4567</p>

    <div class="photo photo-tutor" role="img" aria-label="Photo of a smiling trainer in a white shirt in a classroom"></div>
    <div class="photo photo-student" role="img" aria-label="Photo of a student seated at a desk in a classroom"></div>
    <div class="photo photo-practical" role="img" aria-label="Photo of a trainee working with an anatomy model"></div>

    <ul class="topics">
      <li>Pathology</li>
      <li>Anaphylaxis</li>
      <li>Medicitaions for PCA's</li>
      <li>Aged Care</li>
      <li>First Aid</li>
      <li>CPR</li>
      <li>Home &amp; Community Care</li>
      <li>Health Services</li>
    </ul>
  </main>
</body>
</html>
```